Online Digital Solutions Agency needs a New Business Card

We are a Online/Digital solution agency. We provide WordPress Solutions, Online & Digital Marketing Solutions including SEO, Social Media Marketing and Managed Hosting including VPS and Cloud Hosting solutions. We also design and build bespoke web sites and web applications for various clients. We are very good at site migrations, 3rd party API integrations and mobile app development.

We are rebranding our agency and have already designed a new logo. We have selected 5-6 colours as our base colour and are currently building our new website based around these colour scheme.

Our logo indicates that we are a cloud solution providers, and (i.e. the Clouds), and developers (i.e. HTML Tags, and CSS formats). We use the 5-6 base colours and use various shades of these colours as required.

Our old website is located at: www.brambleforgelabs.com

And our new website is going to be at (we are working on it at the moment ...):
https://creative.brambleforgelabs.co.uk/

Our slogan is "Digital Transformation Specialist"

What we mean by that is; we can take any existing business and get them up and transform them in to the digital world, starting with Hosting, Web Design, Development & Online Marketing aspects.

The powerpoint is a document that we use to present our projects to clients at the moment, and the cloud is on the background as we clarified earlier. (Just to get the idea)

What we are looking for is a Great WoW factor design to start with, ideally with the Logo and Logo colour scheme if possible but not required as long as the designers can do better, and basically give life to our logo and company via the Business card design.

Ideally with some icons perhaps to indicate the address, location, mobile, email, and website would be good but again optional as long as there is a good design.

The cloud can be used as a background if required in a light shade or as a watermark share perhaps.

The logos' and the Illustrator files are shared with you so you can use them as required.

Ideally the business card should have a Name, title, Mobile, Email , Website, Address and perhaps some social media links.

Target Market(s)

New Startups, SME's, Contract and Outsource Clients

Contact Information for Business Card

Company Name:
==============
BrambleForge Labs (UK) Ltd.

Tag Line:
========
“Digital Transformation Specialists”

Adress:
=======

Suite KR73054
14-16 Ashgrove Lane
London
E9 4PD.

Name:
=====
Idris Malek

Title: (Optional)
=============
FQTA, PgD (RNOM)

Role:
=====
Digital Solutions Architect

Email:
=====
idris@brambleforgelabs.uk

WebSite:
=======
http://www.brambleforgelabs.uk

OR

www.brambleforgelabs.uk

Mobile:
======
0044 (0)75 218 30479

OR

+44 (0)75 218 30479

LinkedIN: (Optional)
========
https://uk.linkedin.com/in/idrismalek

Skype: (Optional)
======
idris.malek

Twitter (Optional) : idrismalek

Font styles to use
Serif
Sans Serif

Requirements
Must have
• The Logo
• Business Name
• Person Name
• Title
• Mobile
• Email
• Website
• Address
• I have provided the colour scheme on my files.
Nice to have
• Twiter
• Linked in
• Facebook

```html
<!DOCTYPE html>
<html lang="en">
<head>
<meta charset="utf-8">
<title>BrambleForge Labs — Business Card</title>
<link rel="stylesheet" href="https://fonts.googleapis.com/css2?family=Montserrat:wght@500;700;800&family=Roboto:wght@400;700&display=swap">
<style>
  :root {
    --bg: #2b2b2b;
    --card: #ffffff;
    --card-shade: #ececec;
    --navy: #0f4f99;
    --royal: #1c63b0;
    --sky: #4fb3d9;
    --sky-light: #7fcbe8;
    --ink: #1d1d1d;
    --tag: #4a7fc0;
  }
  * { margin: 0; padding: 0; box-sizing: border-box; }
  html, body { width: 1200px; height: 997px; overflow: hidden; }
  body {
    background: var(--bg);
    display: flex;
    align-items: center;
    justify-content: center;
    gap: 40px;
    font-family: "Roboto", Arial, sans-serif;
  }
  .card {
    position: relative;
    width: 540px;
    height: 310px;
    background: linear-gradient(160deg, var(--card) 40%, var(--card-shade));
    overflow: hidden;
    border-radius: 2px;
  }
  .card-bands { position: absolute; inset: 0; width: 100%; height: 100%; }

  .brand {
    display: flex;
    align-items: center;
    gap: 10px;
    font-family: "Montserrat", Arial, sans-serif;
    font-weight: 800;
    color: var(--navy);
    white-space: nowrap;
  }
  .brand-dot {
    border-radius: 50%;
    background: var(--sky);
    flex: none;
  }

  /* front */
  .card-front .brand {
    position: absolute;
    left: 0; right: 0; top: 92px;
    justify-content: center;
    font-size: 38px;
  }
  .card-front .brand-dot { width: 22px; height: 22px; }
  .tagline {
    position: absolute;
    left: 0; right: 0; top: 160px;
    text-align: center;
    font-family: "Montserrat", Arial, sans-serif;
    font-weight: 700;
    font-size: 12.5px;
    letter-spacing: 1.6px;
    color: var(--tag);
  }

  /* back */
  .card-back .brand {
    position: absolute;
    left: 150px; top: 58px;
    font-size: 30px;
  }
  .card-back .brand-dot { width: 18px; height: 18px; }
  .holder {
    position: absolute;
    right: 36px; top: 130px;
    text-align: right;
  }
  .holder-name {
    font-weight: 700;
    font-size: 13px;
    color: var(--navy);
    letter-spacing: .3px;
  }
  .holder-role { font-size: 11.5px; color: var(--ink); margin-top: 2px; }

  .contact-tab {
    position: absolute;
    left: 0; top: 186px;
    width: 26px; height: 84px;
    background: var(--navy);
    border-radius: 0 6px 6px 0;
    display: flex;
    flex-direction: column;
    justify-content: space-around;
    align-items: center;
    padding: 4px 0;
  }
  .contact-tab svg { width: 12px; height: 12px; }
  .contact-list {
    position: absolute;
    left: 40px; top: 188px;
    list-style: none;
    font-family: "Montserrat", Arial, sans-serif;
    font-weight: 500;
    font-size: 12px;
    color: var(--ink);
    line-height: 20px;
  }
</style>
</head>
<body>

  <section class="card card-front" aria-label="Business card front">
    <svg class="card-bands" viewBox="0 0 540 310" preserveAspectRatio="none" aria-hidden="true">
      <path d="M300 310 C318 282 330 274 360 274 L540 262 L540 310 Z" fill="var(--royal)"/>
      <path d="M0 310 L0 290 L330 286 C318 296 312 302 308 310 Z" fill="var(--sky-light)"/>
    </svg>
    <div class="brand"><span class="brand-dot"></span>BrambleForge Labs</div>
    <p class="tagline">DIGITAL TRANSFORMATION SPECIALISTS</p>
  </section>

  <section class="card card-back" aria-label="Business card back">
    <svg class="card-bands" viewBox="0 0 540 310" preserveAspectRatio="none" aria-hidden="true">
      <path d="M360 252 C372 236 384 232 404 230 L540 206 L540 248 Z" fill="var(--navy)"/>
      <path d="M0 310 L0 292 L380 250 L540 226 L540 248 L380 276 L360 290 L0 310 Z" fill="var(--sky)"/>
      <path d="M0 310 L0 300 L540 254 L540 310 Z" fill="var(--sky-light)"/>
    </svg>

    <div class="brand"><span class="brand-dot"></span>BrambleForge Labs</div>

    <div class="holder">
      <p class="holder-name">IDRIS MALEK</p>
      <p class="holder-role">Digital Solutions Architect</p>
    </div>

    <div class="contact-tab" aria-hidden="true">
      <svg viewBox="0 0 12 12"><rect x="3" y="0.5" width="6" height="11" rx="1.2" fill="none" stroke="#fff" stroke-width="1.2"/><circle cx="6" cy="9.6" r=".7" fill="#fff"/></svg>
      <svg viewBox="0 0 12 12"><rect x="0.8" y="2.5" width="10.4" height="7" fill="none" stroke="#fff" stroke-width="1.1"/><path d="M1 3 L6 7 L11 3" fill="none" stroke="#fff" stroke-width="1.1"/></svg>
      <svg viewBox="0 0 12 12"><circle cx="6" cy="6" r="5" fill="#fff"/></svg>
      <svg viewBox="0 0 12 12"><circle cx="6" cy="6" r="5" fill="#fff"/></svg>
    </div>
    <ul class="contact-list">
      <li>0044 (0)75 218 30479</li>
      <li>idris@brambleforgelabs.uk</li>
      <li>idrismalek</li>
      <li>idrismalek</li>
    </ul>
  </section>

</body>
</html>
```